Painting Company Business Card

Brightwell Painting needs a new business card. See attachments for our logo and current card as an example.
We want to utilize the same colors in the logo, and keep all the information that is currently on it. Just need an updated and modern design.
We are open to loosing the Association Logos if it means a better design.
We are also entertaining a spot for a picture of a headshot of the person listed on the card. Head shot can be finished later.

```html
<!DOCTYPE html>
<html lang="en">
<head>
<meta charset="utf-8">
<title>Brightwell Painting – Business Card</title>
<link rel="stylesheet" href="https://fonts.googleapis.com/css2?family=Roboto:wght@400;500;700&display=swap">
<style>
  :root {
    --green-dark: #2f4226;
    --green: #3f5a2e;
    --green-light: #4b6a35;
    --brown: #6b3131;
    --white: #ffffff;
    --ink: #2b2b2b;
    --icon: #6b6b6b;
    --backdrop: #e9e6e1;
  }
  * { margin: 0; padding: 0; box-sizing: border-box; }
  html, body { width: 1200px; height: 800px; overflow: hidden; }
  body {
    background: var(--backdrop);
    font-family: "Roboto", Arial, sans-serif;
    position: relative;
  }
  .card {
    position: absolute;
    width: 520px;
    height: 300px;
    border-radius: 6px;
    overflow: hidden;
    box-shadow: 0 6px 18px rgba(0,0,0,0.18);
  }

  /* Back face: services */
  .card-back {
    left: 50px; top: 250px;
    background: radial-gradient(circle at 45% 55%, var(--green-light), var(--green-dark) 85%);
    color: var(--white);
  }
  .card-back .brand-mark {
    position: absolute; right: 26px; top: 24px;
    font-weight: 700; font-size: 20px; color: var(--white);
    opacity: 0.9;
  }
  .services {
    list-style: none;
    position: absolute; left: 50px; top: 104px;
  }
  .services li {
    display: flex; align-items: center; gap: 18px;
    font-weight: 500; font-size: 19px; letter-spacing: 4px;
    text-transform: uppercase; margin-bottom: 14px;
  }
  .services svg { width: 22px; height: 22px; flex: none; }

  /* Front face: contact */
  .card-front {
    left: 630px; top: 250px;
    background: linear-gradient(160deg, var(--green-light), var(--green-dark));
  }
  .card-front .white-panel { position: absolute; inset: 0; width: 100%; height: 100%; }
  .brand-name {
    position: absolute; right: 34px; top: 62px;
    font-weight: 700; font-size: 38px; line-height: 1.05;
    color: var(--green-dark); text-align: right;
  }
  .name-band {
    position: absolute; right: 0; top: 192px;
    width: 240px; height: 30px;
    background: var(--brown);
    clip-path: polygon(5% 0, 100% 0, 100% 100%, 0 100%);
    color: var(--white); font-size: 18px;
    display: flex; align-items: center; justify-content: flex-end;
    padding-right: 20px;
  }
  .job-title {
    position: absolute; right: 20px; top: 228px;
    font-size: 12px; color: var(--ink);
  }
  .contact-list { list-style: none; position: absolute; left: 0; top: 160px; }
  .contact-list li {
    display: flex; align-items: center; height: 30px; margin-bottom: 8px;
    color: var(--white); font-size: 14px; white-space: nowrap;
  }
  .contact-list .tab {
    width: 70px; height: 22px; background: var(--white);
    clip-path: polygon(0 0, 82% 0, 100% 100%, 0 100%);
    display: flex; align-items: center; justify-content: flex-end;
    padding-right: 18px; margin-right: 10px; flex: none;
  }
  .contact-list .tab svg { width: 13px; height: 13px; }
</style>
</head>
<body>

<section class="card card-back" aria-label="Business card back">
  <div class="brand-mark">Brightwell Painting</div>
  <ul class="services">
    <li><svg viewBox="0 0 24 24" fill="none" stroke="#fff" stroke-width="2.4"><rect x="2" y="4" width="18" height="18" rx="2"/><path d="M6 12l4 4 12-12"/></svg>Exterior Painting</li>
    <li><svg viewBox="0 0 24 24" fill="none" stroke="#fff" stroke-width="2.4"><rect x="2" y="4" width="18" height="18" rx="2"/><path d="M6 12l4 4 12-12"/></svg>Interior Painting</li>
    <li><svg viewBox="0 0 24 24" fill="none" stroke="#fff" stroke-width="2.4"><rect x="2" y="4" width="18" height="18" rx="2"/><path d="M6 12l4 4 12-12"/></svg>Carpentry</li>
    <li><svg viewBox="0 0 24 24" fill="none" stroke="#fff" stroke-width="2.4"><rect x="2" y="4" width="18" height="18" rx="2"/><path d="M6 12l4 4 12-12"/></svg>Drywall</li>
  </ul>
</section>

<section class="card card-front" aria-label="Business card front">
  <svg class="white-panel" viewBox="0 0 520 300" preserveAspectRatio="none" aria-hidden="true">
    <polygon points="30,0 520,0 520,300 360,300" fill="#ffffff"/>
  </svg>
  <div class="brand-name">Brightwell<br>Painting</div>
  <div class="name-band">Daniel Harper</div>
  <div class="job-title">Quality Manager</div>
  <ul class="contact-list">
    <li><span class="tab"><svg viewBox="0 0 24 24" fill="#6b6b6b"><path d="M6.6 10.8a15 15 0 006.6 6.6l2.2-2.2a1 1 0 011-.25 11.4 11.4 0 003.6.57 1 1 0 011 1V20a1 1 0 01-1 1A17 17 0 013 4a1 1 0 011-1h3.5a1 1 0 011 1c0 1.25.2 2.45.57 3.57a1 1 0 01-.25 1z"/></svg></span>262-555-0148</li>
    <li><span class="tab"><svg viewBox="0 0 24 24" fill="none" stroke="#6b6b6b" stroke-width="2"><circle cx="12" cy="12" r="9"/><path d="M3 12h18M12 3c3 3 3 15 0 18M12 3c-3 3-3 15 0 18"/></svg></span>BrightwellPainting.com</li>
    <li><span class="tab"><svg viewBox="0 0 24 24" fill="none" stroke="#6b6b6b" stroke-width="2"><rect x="3" y="5" width="18" height="14" rx="1"/><path d="M3 6l9 7 9-7"/></svg></span>dan@brightwell.com</li>
  </ul>
</section>

</body>
</html>
```